SunHarbor Business Card Design

We are a program for young adults with special needs. We provide care and recreation throughout the day. We need something that appeals to young adults, their parents and teachers. Our motto is "Building Bridges of Hope in the Lives of Young Adults with Special Needs".

Target Market(s)

Young adults with special needs, parents, teachers

Industry/Entity Type

Recreation

Contact Information for Business Card

SunHarbor at the Willowmere

Tanya Fairclough
SunHarbor Case Manager

4153 Carrow Lane
Maple Ridge NC
(803) 426-8170 (803) 538-2914
email: tanya@sunharborsc.example
website: www.sunharborsc.example

Requirements
Must have
• A Bridge design would be nice and our logo. Earthy and bright colors not too business like.

```html
<!DOCTYPE html>
<html lang="en">
<head>
<meta charset="utf-8">
<title>SunHarbor Business Card</title>
<link rel="stylesheet" href="https://fonts.googleapis.com/css2?family=Cormorant+Garamond:ital,wght@0,600;1,500&family=Montserrat:wght@400;700&display=swap">
<style>
  :root {
    --bg: #e9e6e1;
    --brick: #b8443b;
    --paper: #f3f3f2;
    --ink: #3a3a3a;
    --ink-soft: #555555;
    --rule: #8a8a8a;
    --orange: #f07a22;
    --lime: #a9c61f;
    --crimson: #b22a2a;
    --wine: #7a2a22;
  }
  * { margin: 0; padding: 0; box-sizing: border-box; }
  html, body { width: 1200px; height: 900px; overflow: hidden; }
  body {
    background: var(--bg);
    font-family: "Montserrat", sans-serif;
    color: var(--ink);
    position: relative;
  }
  .card {
    position: absolute;
    left: 285px;
    width: 630px;
    height: 360px;
    box-shadow: 0 6px 18px rgba(0,0,0,0.18);
    overflow: hidden;
  }
  /* Front */
  .card-front { top: 50px; background: var(--brick); }
  .front-brand {
    position: absolute;
    right: 40px; top: 150px;
    text-align: right;
    color: #ffffff;
  }
  .wordmark {
    font-family: "Cormorant Garamond", serif;
    font-weight: 600;
    font-size: 46px;
    line-height: 1;
    letter-spacing: 0.5px;
  }
  .tagline {
    font-family: "Cormorant Garamond", serif;
    font-style: italic;
    font-weight: 500;
    font-size: 13px;
    margin-top: 6px;
    white-space: nowrap;
  }
  /* Back */
  .card-back { top: 490px; background: var(--paper); }
  .contact {
    position: absolute;
    left: 40px; top: 40px;
    width: 300px;
  }
  .person-name { font-weight: 700; font-size: 17px; color: var(--ink); }
  .person-title { font-size: 13px; color: var(--ink-soft); margin-top: 4px; padding-bottom: 10px; border-bottom: 1px solid var(--rule); }
  .contact-list { list-style: none; margin-top: 12px; font-size: 12.5px; color: var(--ink-soft); }
  .contact-list li { display: flex; align-items: center; gap: 10px; margin-bottom: 9px; }
  .contact-list svg { width: 13px; height: 13px; flex: none; }
  .back-brand {
    position: absolute;
    right: 40px; top: 60px;
    text-align: right;
    color: var(--wine);
  }
  .back-brand .tagline { color: var(--crimson); }
  .brand-row { display: inline-flex; align-items: center; gap: 10px; }
  .brand-dot { width: 14px; height: 14px; border-radius: 50%; background: var(--orange); }
  .address {
    position: absolute;
    right: 40px; bottom: 42px;
    width: 280px;
    text-align: right;
    font-size: 13px;
    color: var(--ink);
    border-top: 1px solid var(--rule);
    padding-top: 10px;
    line-height: 1.5;
  }
  .website { color: var(--orange); }
  .accent-band {
    position: absolute;
    left: 0; bottom: 0;
    width: 100%; height: 8px;
    display: flex;
  }
  .accent-band span { height: 100%; }
  .band-orange { width: 30%; background: var(--orange); }
  .band-lime { width: 30%; background: var(--lime); }
  .band-crimson { width: 40%; background: var(--crimson); }
</style>
</head>
<body>
  <section class="card card-front" aria-label="Business card front">
    <div class="front-brand">
      <div class="wordmark">SunHarbor</div>
      <div class="tagline">Opening Brighter Days for Young Adults of Every Ability</div>
    </div>
  </section>

  <section class="card card-back" aria-label="Business card back">
    <div class="contact">
      <div class="person-name">Tanya Fairclough</div>
      <div class="person-title">SunHarbor Case Manager</div>
      <ul class="contact-list">
        <li>
          <svg viewBox="0 0 16 16"><path fill="#f07a22" d="M3 1h3l1.5 4-2 1.3a9 9 0 0 0 4.2 4.2L11 8.5l4 1.5v3c0 1-1 2-2 2A12 12 0 0 1 1 3c0-1 1-2 2-2z"/></svg>
          (803) 426-8170
        </li>
        <li>
          <svg viewBox="0 0 16 16"><path fill="#f07a22" d="M3 1h3l1.5 4-2 1.3a9 9 0 0 0 4.2 4.2L11 8.5l4 1.5v3c0 1-1 2-2 2A12 12 0 0 1 1 3c0-1 1-2 2-2z"/></svg>
          (803) 538-2914
        </li>
        <li>
          <svg viewBox="0 0 16 16"><rect x="1" y="3" width="14" height="10" rx="1" fill="#f07a22"/><path d="M1.5 4l6.5 5 6.5-5" stroke="#fff" stroke-width="1.3" fill="none"/></svg>
          email: tanya@sunharborsc.example
        </li>
      </ul>
    </div>

    <div class="back-brand">
      <div class="brand-row"><span class="brand-dot"></span><span class="wordmark">SunHarbor</span></div>
      <div class="tagline">Opening Brighter Days for Young Adults of Every Ability</div>
    </div>

    <div class="address">
      4153 Carrow Lane<br>
      Maple Ridge NC<br>
      <span class="website">www.sunharborsc.example</span>
    </div>

    <div class="accent-band">
      <span class="band-orange"></span><span class="band-lime"></span><span class="band-crimson"></span>
    </div>
  </section>
</body>
</html>
```